Business Cards

Business cards (double-sided) to be handed out to clients and potential clients, with contact details, logo .

Target Market(s)

Small to medium size businesses

Industry/Entity Type

Accountants

Contact Information for Business Card

Brightwater Ledger & Counsel Ltd

Colors

Designer to choose only greyscale colors for use in the design.

Requirements
Must have
• Name, Title, Address, Phone number, Email, Website
Nice to have
• Modern, clean lines, classy
Should not have
• Business cards to be double-sided. Form keeps reverting to single-sided.

```html
<!DOCTYPE html>
<html lang="en">
<head>
<meta charset="utf-8">
<title>Brightwater Ledger &amp; Counsel Ltd — Business Card</title>
<link rel="stylesheet" href="https://fonts.googleapis.com/css2?family=Josefin+Sans:wght@300;400;500&display=swap">
<style>
  :root {
    --backdrop: #e4e5e7;
    --ink: #000000;
    --paper: #ffffff;
    --rule: #000000;
  }
  * { margin: 0; padding: 0; box-sizing: border-box; }
  html, body {
    width: 1200px;
    height: 1200px;
    overflow: hidden;
    background: var(--backdrop);
    font-family: "Josefin Sans", sans-serif;
  }
  .canvas {
    position: relative;
    width: 1200px;
    height: 1200px;
  }
  .card {
    position: absolute;
    left: 235px;
    width: 730px;
    height: 442px;
  }
  .card--front {
    top: 130px;
    background: var(--ink);
    display: flex;
    align-items: center;
    justify-content: center;
  }
  .brand-name {
    color: var(--paper);
    font-weight: 400;
    font-size: 28px;
    letter-spacing: 0.12em;
    text-transform: uppercase;
    white-space: nowrap;
  }
  .card--back {
    top: 630px;
    background: var(--paper);
  }
  .contact-grid {
    display: block;
    width: 100%;
    height: 100%;
  }
  .contact-grid line {
    stroke: var(--rule);
    stroke-width: 2;
    stroke-linecap: square;
  }
  .contact-grid text {
    fill: var(--ink);
    font-family: "Josefin Sans", sans-serif;
    text-anchor: middle;
  }
  .contact-name { font-size: 29px; font-weight: 400; }
  .contact-phone-area { font-size: 40px; font-weight: 300; }
  .contact-phone-number { font-size: 33px; font-weight: 300; }
  .contact-detail { font-size: 20px; font-weight: 300; letter-spacing: 0.03em; }
</style>
</head>
<body>
<main class="canvas">
  <section class="card card--front" aria-label="Card front">
    <h1 class="brand-name">Brightwater Ledger &amp; Counsel Ltd</h1>
  </section>

  <section class="card card--back" aria-label="Card back">
    <svg class="contact-grid" viewBox="0 0 730 442" xmlns="http://www.w3.org/2000/svg">
      <g class="grid-rules">
        <line x1="94" y1="104" x2="642" y2="104"/>
        <line x1="94" y1="339" x2="642" y2="339"/>
        <line x1="94" y1="104" x2="94" y2="339"/>
        <line x1="642" y1="104" x2="642" y2="339"/>
        <line x1="390" y1="104" x2="390" y2="221"/>
        <line x1="390" y1="280" x2="390" y2="339"/>
        <line x1="94" y1="162" x2="390" y2="162"/>
        <line x1="94" y1="221" x2="642" y2="221"/>
        <line x1="94" y1="280" x2="642" y2="280"/>
      </g>
      <text class="contact-name" x="243" y="146">YOUR NAME</text>
      <text class="contact-detail" x="243" y="200">Your Designation</text>
      <text class="contact-phone-area" x="516" y="160">(800)</text>
      <text class="contact-phone-number" x="516" y="207">123-4567</text>
      <text class="contact-detail" x="368" y="258">Your Company Address Here</text>
      <text class="contact-detail" x="249" y="317">Your Email Address</text>
      <text class="contact-detail" x="517" y="317">Your Website</text>
    </svg>
  </section>
</main>
</body>
</html>
```